Rhythmic Gymnastics Web Design Built in Elementor - Mobile First (adaptable)

I am looking for an elite web designer to work with continuously.
Our goal with this contest is to find someone who can create custom designs (not from templates).
For this test we will be starting with one home page design and if we like the design we will move forward with you to work on more designs for the rest of the site and other sites
I have added a logo and brand colors of the company below.
Some images that can be used - https://files.novarepo.net/folders/8kQmR2tLxW4pZ7yNc3Hv9JdS5bF6gT1?usp=sharing
Brand guide - https://files.novarepo.net/file/d/7pHrTk2MwQ9xLz4Vb8NcJ5sYd3Ef6Ga/view?usp=sharing
Logo-
https://files.novarepo.net/folders/9mWzK4qTxR2vLp8Hn5Bc7JyF3Gd6Sa?usp=sharing
Name of company is Tavisk Gymnastics
Some more images and company info - https://files.novarepo.net/folders/4nVtY8pRzK3wMq7Jc2Hx6LbG9Fd5Ts1?usp=sharing
Please make a mobile first design that can be adaptable for desktop
Navigation - Home, About, Schedule, Coaches, Facility, Results, Competitions, FAQ, Contact
Above the fold Hero **
Headline - LA's Elite Rhythmic Gymnastics - Confidence, Flexibility, Grace, & Results
Coach-led classes for ages 3-17. Flexible schedule. First session Free.
CTA - Free Trial
Trust Strip**
Program section (cards)**
Why choose us section**
Results/Social Proof Section**
testimonaial carousel
Schedule teaser section**
Pricing & Offers**
Coaches You'll Love section (cards)**
Facility Tour section**
Conversion Magnet (lead capture)**
A small box or band on the homepage that says:
“Not ready to book? Get our free First Ribbon Steps Family Handbook.”
They enter Parent Name + Email + Child Age → they instantly get a helpful PDF and a friendly follow-up sequence. No hard sell.
FAQ's Section**
Location, hours, Parking section**
Map embed, service‑area chips (Maple Ridge, Corvale, Westbrook, etc.), hours table, contact block (Call, SMS, WhatsApp, Email, IG/TikTok).
Footer section with quick links**
Target Market(s)
That target market is parents of girls
Industry/Entity Type
Rhythmic Gymnastics
Font styles to use
Look and feel
Each slider illustrates characteristics of the customer's brand and the style your logo design should communicate.

```html
<!DOCTYPE html>
<html lang="en">
<head>
<meta charset="utf-8">
<title>Tavisk Gymnastics – Mobile Home</title>
<link href="https://fonts.googleapis.com/css2?family=Playball&family=Poppins:wght@400;500;600&display=swap" rel="stylesheet">
<style>
:root{
  --page:#0a1030;
  --navy:#0c1440;
  --navy-deep:#070c28;
  --royal:#1a2c80;
  --royal-2:#21379a;
  --sky:#4e92d6;
  --sky-soft:#6aa6e0;
  --purple:#a23fd4;
  --purple-2:#c060e0;
  --white:#ffffff;
  --muted:#c9d2ee;
  --line:#2d4aa8;
}
*{box-sizing:border-box;margin:0;padding:0}
html,body{width:1200px;height:3075px;overflow:hidden}
body{background:var(--page);font-family:'Poppins',sans-serif;color:var(--white);position:relative}
.col{position:absolute;width:263px;display:flex;flex-direction:column;overflow:hidden}
.col-1{left:140px;top:90px;height:2985px;border:1px solid var(--line);border-bottom:none;border-radius:14px 14px 0 0}
.col-2{left:478px;top:0;height:3075px}
.col-3{left:815px;top:0;height:3075px;border-left:1px solid var(--line);border-right:1px solid var(--line)}
section{position:relative;flex:none;text-align:center;overflow:hidden}
.title{font-family:'Playball',cursive;font-size:25px;line-height:1.2}
.sub{font-size:8px;line-height:1.55;color:var(--white)}
.eyebrow{font-family:'Playball',cursive;color:var(--sky-soft);font-size:15px}
.btn{display:inline-block;border-radius:30px;font-weight:600;font-size:9px;text-align:center}
.btn-purple{background:linear-gradient(90deg,var(--purple),var(--purple-2));padding:8px 30px}
.btn-outline{border:2px solid var(--white);padding:9px 36px;font-size:10px}
.dots{display:flex;gap:8px;justify-content:center}
.dots i{width:4px;height:4px;border-radius:50%;border:1px solid var(--white);display:block}
.dots i.on{background:var(--white)}
.wave{position:absolute;left:0;width:100%}
.photo{display:block}

/* column 1 */
.hero{height:418px;background:linear-gradient(180deg,var(--royal) 0%,var(--navy) 45%,var(--royal-2) 100%)}
.topbar{margin:16px 12px 0;height:50px;border-radius:8px;background:var(--royal-2);display:flex;align-items:center;justify-content:space-between;padding:0 12px;border:1px solid var(--line)}
.brand{font-family:'Poppins',sans-serif;font-size:12px;font-weight:500;display:flex;align-items:center;gap:6px}
.brand b{width:9px;height:9px;border-radius:50%;background:var(--white);display:block}
.burger{width:14px;display:flex;flex-direction:column;gap:3px}
.burger i{height:2px;background:var(--white);display:block}
.hero-kicker{font-family:'Playball',cursive;font-size:12px;margin-top:30px}
.hero-title{font-family:'Playball',cursive;font-size:16px;margin-top:4px}
.hero .sub{margin:14px 30px 0;font-size:7.5px}
.hero-photo{position:absolute;left:0;bottom:0;width:100%;height:186px;background:linear-gradient(160deg,#5a4fa6 0%,#2a3e9a 45%,#7b8fd0 100%)}
.hero-cta{position:absolute;left:50%;transform:translateX(-50%);top:188px;padding:9px 20px}
.trust{height:185px;background:var(--navy);padding-top:14px}
.trust-item{margin:0 30px 12px;height:34px;border-radius:8px;background:var(--navy-deep);box-shadow:0 0 8px rgba(78,146,214,.55);display:flex;align-items:center;gap:16px;padding-left:18px;font-size:8px}
.trust-item svg{width:14px;height:14px}
.program{height:424px;background:var(--navy);padding-top:36px}
.program-card{margin:20px 30px 0;height:220px;border-radius:8px;overflow:hidden;position:relative;background:var(--sky)}
.program-card .photo{height:148px;background:linear-gradient(180deg,#b8283a 0%,#e9dcd8 40%,#c6b7c4 100%)}
.program-card .info{position:absolute;left:0;bottom:0;width:100%;padding:0 12px 14px;text-align:left}
.program-card .info h4{font-family:'Playball',cursive;font-size:17px;font-weight:400}
.program-card .info p{font-size:7px;line-height:1.5}
.round-arrow{position:absolute;left:20px;width:26px;height:26px;border-radius:50%;background:var(--purple);display:flex;align-items:center;justify-content:center}
.program .dots{margin-top:36px}
.program .btn-outline{margin-top:18px}
.why{height:561px;background:var(--navy);text-align:left;padding:50px 22px 0}
.why .title{font-size:24px}
.why-photo{height:144px;border-radius:12px;margin-top:12px;background:linear-gradient(180deg,#eaeef8 0%,#cdd5ea 60%,#d8cfe4 100%)}
.why p{font-size:7px;line-height:1.85;margin-top:30px}
.why p+p{margin-top:12px}
.why .btn{margin-top:32px;padding:9px 30px}
.testi{height:400px;background:var(--royal);text-align:left;padding:66px 22px 0}
.testi .title{font-size:23px}
.testi-card{margin:18px 18px 0;height:174px;border-radius:6px;background:var(--white);color:#333;padding:12px}
.stars{display:flex;gap:8px}
.stars svg{width:15px;height:15px}
.testi-card p{font-size:10.5px;line-height:1.4;margin-top:22px;color:#333}
.testi-card .who{text-align:center;margin-top:18px;font-size:11px;font-weight:600;color:#111}
.testi-card .who span{display:block;font-weight:400;color:#888}
.avatar{position:absolute;right:40px;bottom:85px;width:38px;height:38px;border-radius:50%;background:linear-gradient(135deg,#b7a593,#e3d7c8);border:3px solid var(--royal)}
.testi .dots{margin-top:34px}
.schedule{height:998px;background:var(--navy);padding-top:52px}
.schedule .title{font-size:23px}
.schedule .sub{margin-top:10px}
.day{margin:0 30px;height:102px;border-radius:12px;background:var(--navy-deep);border:2px solid var(--navy-deep);box-shadow:0 0 0 2px var(--line),0 0 10px rgba(78,146,214,.6);position:relative;overflow:hidden;display:flex;align-items:center;gap:14px;padding-left:22px;text-align:left}
.day:first-of-type{margin-top:34px}
.day+.day{margin-top:24px}
.day svg.clock{width:30px;height:30px}
.day b{display:block;font-size:16px;font-weight:500}
.day span{font-size:12px;font-weight:500}
.day .wave{bottom:0;height:34px}
.schedule .btn-outline{margin-top:70px;font-size:11px;padding:14px 36px}

/* pricing */
.pricing{height:621px;background:linear-gradient(180deg,var(--royal) 0%,#1b3596 100%);padding-top:70px}
.pricing .title{font-size:26px}
.pricing .sub{margin-top:10px}
.price-card{margin:30px 30px 0;height:262px;border-radius:6px;background:var(--navy-deep);position:relative;overflow:hidden}
.price-card h3{font-family:'Playball',cursive;font-weight:400;color:var(--sky-soft);font-size:25px;padding-top:16px}
.price-card .tag{font-family:'Playball',cursive;font-size:14px}
.price-card .amount{color:var(--sky-soft);font-size:17px;font-weight:600;margin-top:6px}
.price-card .amount small{font-size:8px;color:var(--white);font-weight:400}
.price-list{position:absolute;left:8px;right:8px;bottom:0;height:140px;background:var(--sky);border-radius:0 0 6px 6px;text-align:left;padding:30px 0 0 24px}
.price-list li{list-style:none;font-size:8.5px;display:flex;gap:8px;align-items:center;margin-bottom:10px}
.book{position:absolute;left:50%;transform:translateX(-50%);background:var(--navy-deep);font-size:8.5px;padding:6px 14px;border-radius:12px}
.pricing .dots{margin-top:40px}
.pricing .btn-outline{margin-top:18px;padding:10px 36px;font-size:11px}
.coaches{height:770px;background:var(--navy);padding-top:30px}
.coaches .title{font-size:24px;margin-top:30px}
.coaches .sub{margin:12px 22px 0}
.coach-card{margin:16px 13px 0;height:500px;border-radius:8px;background:var(--navy-deep);border:2px solid var(--line);box-shadow:0 0 10px rgba(78,146,214,.5);padding:8px;text-align:left}
.coach-photo{height:190px;border-radius:4px;background:linear-gradient(120deg,#f4f1ec 0%,#dcd7d0 60%,#c8c0b6 100%)}
.coach-card h4{font-size:16px;font-weight:500;margin-top:16px}
.coach-card .role{font-size:8px}
.coach-card .label{font-size:8.5px;font-weight:500;margin-top:16px}
.skill{display:flex;gap:8px;margin-top:12px;font-size:7px;line-height:1.55}
.skill svg{flex:none;width:14px;height:14px}
.skill b{font-weight:600}
.coach-card .btn{margin-top:14px;padding:7px 20px}
.coaches .dots{margin-top:40px}
.coaches .btn-outline{margin-top:18px;font-size:11px;padding:10px 30px}
.facility{height:400px;background:var(--navy);padding-top:70px}
.facility .title{font-size:24px}
.facility .sub{margin:12px 22px 0}
.facility-photo{margin:20px 16px 0;height:142px;border-radius:8px;border:2px solid var(--sky);background:linear-gradient(180deg,#8c8f98 0%,#c4c1ba 45%,#b08a5e 100%)}
.facility .dots{margin-top:24px;gap:20px}
.lead{height:519px;background:linear-gradient(180deg,var(--royal) 0%,#1a2f88 100%);padding-top:88px}
.col-3 .lead{height:621px;padding-top:196px}
.lead .title{font-size:20px}
.lead .sub{margin:10px 30px 0}
.lead-form{margin:20px 10px 0;background:var(--navy-deep);border-radius:12px;padding:10px 10px;display:flex;flex-direction:column;gap:13px}
.field{height:45px;border-radius:24px;border:1px solid var(--sky);background:var(--royal);text-align:left;padding-left:18px;display:flex;align-items:center;font-size:10px}
.send{height:48px;border-radius:24px;background:linear-gradient(90deg,var(--purple),var(--purple-2));display:flex;align-items:center;justify-content:center;font-weight:600;font-size:11px}
.lead .note{font-size:8px;line-height:1.5;margin:30px 40px 0}
.faq{height:543px;background:var(--navy);padding-top:78px}
.faq .title{font-size:20px}
.faq .sub{margin:12px 40px 0}
.faq-open{margin:28px 8px 0;background:var(--sky);border-radius:6px;text-align:left;padding:14px 12px;height:94px}
.faq-open h5{font-size:11px;font-weight:400;display:flex;justify-content:space-between}
.faq-open p{font-size:7px;line-height:1.4;margin-top:14px;color:#e8f0ff}
.faq-item{margin:12px 8px 0;background:var(--white);color:#222;border-radius:3px;height:32px;display:flex;align-items:center;justify-content:space-between;padding:0 8px;font-size:9px;text-align:left}
.faq .btn-outline{margin-top:24px;padding:10px 32px;font-size:9.5px}
.connect{height:222px;background:var(--navy);padding-top:60px}
.connect .title{font-size:20px}
.connect .sub{margin:12px 40px 0}
.contact-head{font-family:'Playball',cursive;font-size:15px;margin-top:26px}
.contact-line{width:120px;height:2px;background:var(--sky);margin:8px auto 0}
.contact-row{display:flex;gap:14px;text-align:left;font-size:10.5px;line-height:1.45;margin:20px 0 0 36px;align-items:flex-start}
.contact-row svg{flex:none;width:14px;height:14px;margin-top:2px}

/* column 3 */
.dots-top{position:absolute;top:18px;left:0;width:100%;gap:20px}
.top-cover{position:absolute;top:0;left:0;width:100%;height:72px;background:var(--navy)}
.connect-full{height:1093px;background:var(--navy);padding-top:80px}
.connect-full .title{font-size:20px}
.connect-full .sub{margin:12px 40px 0}
.follow{font-size:11.5px;margin-top:46px}
.socials{display:flex;gap:10px;justify-content:center;margin-top:12px}
.socials i{width:11px;height:11px;border-radius:50%;background:var(--sky);display:block}
.hours{margin:34px 30px 0;text-align:left}
.hours div{display:flex;font-size:10.5px;border-bottom:1px solid #3a4a84;padding:10px 0 13px}
.hours div:last-child{border:none}
.hours span:first-child{width:74px;flex:none}
.map{margin:40px 8px 0;height:238px;border-radius:8px;background:linear-gradient(135deg,#e8ebf0 0%,#d8dde6 100%)}
.footer{height:818px;background:linear-gradient(180deg,var(--royal) 0%,#16266e 70%,var(--royal) 100%);text-align:left;padding:120px 18px 0}
.footer-brand{font-size:20px;font-weight:500;display:flex;align-items:center;gap:10px;white-space:nowrap}
.footer-brand b{width:14px;height:14px;border-radius:50%;background:var(--white);display:block;flex:none}
.footer p{font-size:6.5px;line-height:1.6;margin-top:14px}
.footer a{color:var(--purple-2);font-size:6.5px;text-decoration:underline}
.f-label{font-size:8.5px;margin-top:28px}
.footer .socials{justify-content:flex-start;margin-top:12px}
.f-head{font-family:'Playball',cursive;color:var(--purple-2);font-size:15px;margin-top:30px}
.f-links li{list-style:none;font-size:7px;margin-top:14px;display:flex;gap:8px;align-items:center}
.f-links li::before{content:"";border-left:3px solid transparent;border-right:3px solid transparent;border-top:4px solid var(--purple-2)}
.f-contact{font-size:7px;display:flex;gap:8px;align-items:center;margin-top:12px}
.f-contact svg{width:11px;height:11px}
.news{margin-top:18px;width:182px;height:30px;border-radius:16px;background:var(--white);color:#aaa;font-size:6.5px;display:flex;align-items:center;justify-content:space-between;padding:0 3px 0 12px}
.news i{width:25px;height:25px;border-radius:50%;background:var(--sky);display:flex;align-items:center;justify-content:center}
.copy{position:absolute;left:0;bottom:0;width:100%;height:48px;background:var(--navy-deep);text-align:center;font-size:6.5px;padding-top:16px;line-height:1.8}
.copy span{color:var(--muted)}
</style>
</head>
<body>

<div class="col col-1">
  <section class="hero">
    <div class="topbar">
      <div class="brand"><b></b>Tavisk Gymnastics</div>
      <div class="burger"><i></i><i></i><i></i></div>
    </div>
    <div class="hero-kicker">LA's Elite Rhythmic Gymnastics</div>
    <div class="hero-title">Confidence, Flexibility, Grace, &amp; Results</div>
    <p class="sub">Coach-Led Classes For Ages 3-17. Flexible Schedule. First Session Free.</p>
    <div class="hero-photo" role="img" aria-label="Group of rhythmic gymnasts performing with ribbons and balls"></div>
    <svg class="wave" style="bottom:0;height:40px" viewBox="0 0 263 40" preserveAspectRatio="none"><path d="M0 40 L0 28 Q60 0 140 14 Q210 26 263 8 L263 40 Z" fill="#0c1440"/><path d="M0 28 Q60 0 140 14 Q210 26 263 8" stroke="#4e92d6" stroke-width="3" fill="none"/></svg>
    <span class="btn btn-purple hero-cta">Free Trial</span>
  </section>

  <section class="trust">
    <div class="trust-item"><svg viewBox="0 0 16 16"><circle cx="8" cy="5" r="3" fill="none" stroke="#fff"/><path d="M3 14 Q8 7 13 14" stroke="#fff" fill="none"/></svg>Ex-Olympian Coaches</div>
    <div class="trust-item"><svg viewBox="0 0 16 16"><path d="M5 2h6v4a3 3 0 0 1-6 0z M8 9v3 M5 14h6" stroke="#fff" fill="none"/></svg>National Team Experience</div>
    <div class="trust-item"><svg viewBox="0 0 16 16"><circle cx="8" cy="7" r="5" fill="none" stroke="#fff"/><path d="M5 14h6" stroke="#fff"/></svg>Over 10 Years Of Excellence</div>
    <div class="trust-item"><svg viewBox="0 0 16 16"><path d="M2 4h12 M5 4l3 9 3-9" stroke="#fff" fill="none"/></svg>First Class Free</div>
  </section>

  <section class="program">
    <div class="title">Program</div>
    <div class="program-card">
      <div class="photo" role="img" aria-label="Gymnast in pink leotard stretching at a championship"></div>
      <svg class="wave" style="top:108px;height:60px" viewBox="0 0 203 60" preserveAspectRatio="none"><path d="M0 60 L0 36 Q80 40 130 20 Q170 4 203 0 L203 60 Z" fill="#4e92d6"/></svg>
      <div class="info">
        <h4>Little Stars</h4>
        <p>Lorem Ipsum Dolor Sit Amet, Consectetur Adipiscing Elit, Sed Do Eiusmod Tempor</p>
      </div>
    </div>
    <div style="position:relative;margin:0 30px;height:0"><span class="round-arrow" style="bottom:-14px"><svg width="14" height="8" viewBox="0 0 14 8"><path d="M0 4h12 M9 1l3 3-3 3" stroke="#fff" fill="none"/></svg></span></div>
    <div class="dots"><i></i><i></i><i></i></div>
    <span class="btn btn-outline">View All Program</span>
  </section>

  <section class="why">
    <svg class="wave" style="top:0;height:40px" viewBox="0 0 263 40" preserveAspectRatio="none"><path d="M0 28 Q130 -14 263 32" stroke="#4e92d6" stroke-width="2.5" fill="none"/></svg>
    <div class="eyebrow">Know More</div>
    <div class="title">Why Choose Us</div>
    <div class="why-photo" role="img" aria-label="Gymnast with ribbon in a bright training hall"></div>
    <p>Sed Ut Perspiciatis Unde Omnis Iste Natus Error Sit Voluptatem Accusantium Doloremque Laudantium, Totam Rem Aperiam, Eaque Ipsa Quae Ab Illo Inventore Veritatis Et Quasi Architecto Beatae Vitae Dicta Sunt Explicabo. Nemo Enim Ipsam Voluptatem Quia Voluptas Sit Aspernatur Aut Odit Aut Fugit, Sed Quia Consequuntur Magni Dolores.</p>
    <p>Eos Qui Ratione Voluptatem Sequi Nesciunt. Neque Porro Quisquam Est, Qui Dolorem Ipsum Quia Dolor Sit Amet, Consectetur, Adipisci Velit, Sed Quia Non Numquam Eius Modi Tempora Incidunt Ut Labore Et Dolore Magnam Aliquam Quaerat Voluptatem.</p>
    <span class="btn btn-purple">Read More About Us</span>
  </section>

  <section class="testi">
    <svg class="wave" style="top:0;height:60px" viewBox="0 0 263 60" preserveAspectRatio="none"><path d="M0 0 L263 0 L263 12 Q220 60 120 30 Q50 12 0 30 Z" fill="#0c1440"/><path d="M263 12 Q220 60 120 30" stroke="#4e92d6" stroke-width="3" fill="none"/></svg>
    <div class="eyebrow">Testimonial</div>
    <div class="title">Client Success Stories</div>
    <div class="testi-card">
      <div class="stars">
        <svg viewBox="0 0 20 20"><path d="M10 1l2.8 6 6.2.6-4.7 4.2 1.4 6.2L10 14.8 4.3 18l1.4-6.2L1 7.6 7.2 7z" fill="#2f6fe0"/></svg>
        <svg viewBox="0 0 20 20"><path d="M10 1l2.8 6 6.2.6-4.7 4.2 1.4 6.2L10 14.8 4.3 18l1.4-6.2L1 7.6 7.2 7z" fill="#2f6fe0"/></svg>
        <svg viewBox="0 0 20 20"><path d="M10 1l2.8 6 6.2.6-4.7 4.2 1.4 6.2L10 14.8 4.3 18l1.4-6.2L1 7.6 7.2 7z" fill="#2f6fe0"/></svg>
        <svg viewBox="0 0 20 20"><path d="M10 1l2.8 6 6.2.6-4.7 4.2 1.4 6.2L10 14.8 4.3 18l1.4-6.2L1 7.6 7.2 7z" fill="#2f6fe0"/></svg>
        <svg viewBox="0 0 20 20"><path d="M10 1l2.8 6 6.2.6-4.7 4.2 1.4 6.2L10 14.8 4.3 18l1.4-6.2L1 7.6 7.2 7z" fill="#2f6fe0"/></svg>
      </div>
      <p>Lorem ipsum dolor sit amet, consectetur adipiscing elit, sed do eiusmod tempor incididunt ut labore et dolore</p>
      <div class="who">Mira Holt<span>Product Manager</span></div>
    </div>
    <div class="avatar" role="img" aria-label="Client portrait"></div>
    <div class="dots"><i></i><i></i><i></i></div>
  </section>

  <section class="schedule">
    <div class="title">Flexible Weekly Schedule</div>
    <p class="sub">Multiple Class Times To Fit Your Family's Busy Life</p>
    <div class="day"><svg class="clock" viewBox="0 0 30 30"><circle cx="15" cy="15" r="12" fill="none" stroke="#fff" stroke-width="2.5"/><path d="M15 8v7l5 3" stroke="#fff" stroke-width="2.5" fill="none"/></svg><div><b>Monday</b><span>4:00 PM - 8:00 PM</span></div><svg class="wave" viewBox="0 0 200 34" preserveAspectRatio="none"><path d="M40 34 Q150 30 200 0 L200 34 Z" fill="#4e92d6"/></svg></div>
    <div class="day"><svg class="clock" viewBox="0 0 30 30"><circle cx="15" cy="15" r="12" fill="none" stroke="#fff" stroke-width="2.5"/><path d="M15 8v7l5 3" stroke="#fff" stroke-width="2.5" fill="none"/></svg><div><b>Tuesday</b><span>4:00 PM - 8:00 PM</span></div><svg class="wave" viewBox="0 0 200 34" preserveAspectRatio="none"><path d="M40 34 Q150 30 200 0 L200 34 Z" fill="#4e92d6"/></svg></div>
    <div class="day"><svg class="clock" viewBox="0 0 30 30"><circle cx="15" cy="15" r="12" fill="none" stroke="#fff" stroke-width="2.5"/><path d="M15 8v7l5 3" stroke="#fff" stroke-width="2.5" fill="none"/></svg><div><b>Wednesday</b><span>4:00 PM - 8:00 PM</span></div><svg class="wave" viewBox="0 0 200 34" preserveAspectRatio="none"><path d="M40 34 Q150 30 200 0 L200 34 Z" fill="#4e92d6"/></svg></div>
    <div class="day"><svg class="clock" viewBox="0 0 30 30"><circle cx="15" cy="15" r="12" fill="none" stroke="#fff" stroke-width="2.5"/><path d="M15 8v7l5 3" stroke="#fff" stroke-width="2.5" fill="none"/></svg><div><b>Thursday</b><span>4:00 PM - 8:00 PM</span></div><svg class="wave" viewBox="0 0 200 34" preserveAspectRatio="none"><path d="M40 34 Q150 30 200 0 L200 34 Z" fill="#4e92d6"/></svg></div>
    <div class="day"><svg class="clock" viewBox="0 0 30 30"><circle cx="15" cy="15" r="12" fill="none" stroke="#fff" stroke-width="2.5"/><path d="M15 8v7l5 3" stroke="#fff" stroke-width="2.5" fill="none"/></svg><div><b>Friday</b><span>4:00 PM - 8:00 PM</span></div><svg class="wave" viewBox="0 0 200 34" preserveAspectRatio="none"><path d="M40 34 Q150 30 200 0 L200 34 Z" fill="#4e92d6"/></svg></div>
    <div class="day"><svg class="clock" viewBox="0 0 30 30"><circle cx="15" cy="15" r="12" fill="none" stroke="#fff" stroke-width="2.5"/><path d="M15 8v7l5 3" stroke="#fff" stroke-width="2.5" fill="none"/></svg><div><b>Saturday</b><span>4:00 PM - 8:00 PM</span></div><svg class="wave" viewBox="0 0 200 34" preserveAspectRatio="none"><path d="M40 34 Q150 30 200 0 L200 34 Z" fill="#4e92d6"/></svg></div>
    <span class="btn btn-outline">See Full Schedule</span>
  </section>
</div>

<div class="col col-2">
  <section class="pricing">
    <div class="title">Pricing &amp; Offers</div>
    <p class="sub">Flexible Options To Match Your Goals And Budget</p>
    <div class="price-card">
      <h3>Drop-In</h3>
      <div class="tag">Perfect For Trying Us Out</div>
      <div class="amount">$35 <small>Per Class</small></div>
      <svg class="wave" style="top:90px;height:40px;left:8px;width:calc(100% - 16px)" viewBox="0 0 190 40" preserveAspectRatio="none"><path d="M0 40 L0 24 Q60 40 120 22 Q160 10 190 0 L190 40 Z" fill="#4e92d6"/></svg>
      <ul class="price-list">
        <li><svg width="10" height="8" viewBox="0 0 10 8"><path d="M1 4l3 3 5-6" stroke="#fff" fill="none" stroke-width="1.4"/></svg>Single Class Access</li>
        <li><svg width="10" height="8" viewBox="0 0 10 8"><path d="M1 4l3 3 5-6" stroke="#fff" fill="none" stroke-width="1.4"/></svg>All Equipment Provided</li>
        <li><svg width="10" height="8" viewBox="0 0 10 8"><path d="M1 4l3 3 5-6" stroke="#fff" fill="none" stroke-width="1.4"/></svg>Expert Instructions</li>
        <li><svg width="10" height="8" viewBox="0 0 10 8"><path d="M1 4l3 3 5-6" stroke="#fff" fill="none" stroke-width="1.4"/></svg>Flexible Scheduling</li>
      </ul>
    </div>
    <div style="position:relative;height:0"><span class="book" style="bottom:-12px">Book Now</span></div>
    <div class="dots"><i></i><i></i><i></i></div>
    <span class="btn btn-outline">Custom Pricing</span>
    <svg class="wave" style="bottom:0;height:50px" viewBox="0 0 263 50" preserveAspectRatio="none"><path d="M0 50 L0 40 Q80 0 160 18 Q220 32 263 28 L263 50 Z" fill="#0c1440"/><path d="M40 24 Q100 -2 160 18 Q220 32 263 28" stroke="#4e92d6" stroke-width="3" fill="none"/></svg>
  </section>

  <section class="coaches">
    <div class="title">Coaches You'll Love</div>
    <p class="sub">Lorem Ipsum Dolor Sit Amet Consectetur. Lobortis Neque Arcu Consequat Vestibulum.</p>
    <div class="coach-card">
      <div class="coach-photo" role="img" aria-label="Coach practising ribbon routine in a sunlit studio"></div>
      <h4>Nora Vell</h4>
      <div class="role">Expert in Form of Dancing</div>
      <div class="label">Expertise</div>
      <div class="skill"><svg viewBox="0 0 14 14"><path d="M1 7l4 4 8-10" stroke="#c060e0" stroke-width="2" fill="none"/></svg><div><b>Lorem ipsum dolor sit amet consectetur.</b> Lobortis neque arcu consequat vestibulum viverra scelerisque.</div></div>
      <div class="skill"><svg viewBox="0 0 14 14"><path d="M1 7l4 4 8-10" stroke="#c060e0" stroke-width="2" fill="none"/></svg><div><b>Lorem ipsum dolor sit amet consectetur.</b> Lobortis neque arcu consequat vestibulum viverra scelerisque.</div></div>
      <div class="skill"><svg viewBox="0 0 14 14"><path d="M1 7l4 4 8-10" stroke="#c060e0" stroke-width="2" fill="none"/></svg><div><b>Lorem ipsum dolor sit amet consectetur.</b> Lobortis neque arcu consequat vestibulum viverra scelerisque.</div></div>
      <span class="btn btn-purple">MEET NORA</span>
    </div>
    <div class="dots"><i></i><i></i><i></i></div>
    <span class="btn btn-outline">See More Coaches</span>
    <svg class="wave" style="bottom:0;height:40px" viewBox="0 0 263 40" preserveAspectRatio="none"><path d="M0 10 Q90 50 263 0" stroke="#4e92d6" stroke-width="3" fill="none"/></svg>
  </section>

  <section class="facility">
    <div class="title">Facility Tour</div>
    <p class="sub">Lorem Ipsum Dolor Sit Amet Consectetur. Lobortis Neque Arcu Consequat Vestibulum.</p>
    <div class="facility-photo" role="img" aria-label="Empty training hall with wooden floor and tall windows"></div>
    <div class="dots"><i></i><i></i><i></i><i class="on"></i><i></i><i></i><i></i><i></i></div>
  </section>

  <section class="lead">
    <svg class="wave" style="top:0;height:70px" viewBox="0 0 263 70" preserveAspectRatio="none"><path d="M0 0 L263 0 L263 2 Q220 60 120 40 Q50 26 0 30 Z" fill="#0c1440"/><path d="M263 2 Q220 60 120 40" stroke="#4e92d6" stroke-width="3" fill="none"/></svg>
    <div class="title">Not Ready To Book?</div>
    <p class="sub">Get Our Free First Ribbon Steps Family Handbook.</p>
    <div class="lead-form">
      <div class="field">Parent Name*</div>
      <div class="field">Email*</div>
      <div class="field">Child Age*</div>
      <div class="send">SEND</div>
    </div>
    <p class="note">Get A Helpful PDF And A Friendly Follow-Up Sequence. No Hard Sell.</p>
  </section>

  <section class="faq">
    <div class="title">Frequently Asked Questions</div>
    <p class="sub">Lorem Ipsum Dolor Sit Amet Consectetur. Lobortis Neque Arcu.</p>
    <div class="faq-open"><h5>What age groups do you train?<span>–</span></h5><p>We offer classes for girls ages 3 to 17, from beginners taking their first steps in rhythmic gymnastics to competitive athletes training for national and international levels.</p></div>
    <div class="faq-item">How do I sign up for the Free Trial?<span>+</span></div>
    <div class="faq-item">Do you offer competitive training programs?<span>+</span></div>
    <div class="faq-item">Are parents allowed to watch the classes?<span>+</span></div>
    <div class="faq-item">How do I know which class is right for my child?<span>+</span></div>
    <span class="btn btn-outline">Have A Question Connect With Us</span>
  </section>

  <section class="connect">
    <svg class="wave" style="top:0;height:40px" viewBox="0 0 263 40" preserveAspectRatio="none"><path d="M0 28 Q120 -10 263 30" stroke="#4e92d6" stroke-width="2.5" fill="none"/></svg>
    <div class="title">Let's Connect</div>
    <p class="sub">Lorem Ipsum Dolor Sit Amet Consectetur. Lobortis Neque Arcu.</p>
    <div class="contact-head">Contact Information</div>
    <div class="contact-line"></div>
    <div class="contact-row"><svg viewBox="0 0 14 14"><path d="M7 13s-4-4.5-4-7.5a4 4 0 0 1 8 0C11 8.5 7 13 7 13z" stroke="#c060e0" fill="none"/><circle cx="7" cy="5.5" r="1.5" stroke="#c060e0" fill="none"/></svg>Maple Ridge, Corvale,<br>Westbrook,</div>
  </section>
</div>

<div class="col col-3">
  <section class="lead">
    <svg class="wave" style="top:70px;height:80px" viewBox="0 0 263 80" preserveAspectRatio="none"><path d="M0 0 L263 0 L263 20 Q220 80 120 60 Q50 46 0 40 Z" fill="#0c1440"/><path d="M263 20 Q220 80 120 60" stroke="#4e92d6" stroke-width="3" fill="none"/></svg>
    <div class="top-cover"></div>
    <div class="dots dots-top"><i></i><i></i><i></i><i class="on"></i><i></i><i></i><i></i><i></i></div>
    <div class="title">Not Ready To Book?</div>
    <p class="sub">Get Our Free First Ribbon Steps Family Handbook.</p>
    <div class="lead-form">
      <div class="field">Parent Name*</div>
      <div class="field">Email*</div>
      <div class="field">Child Age*</div>
      <div class="send">SEND</div>
    </div>
    <p class="note">Get A Helpful PDF And A Friendly Follow-Up Sequence. No Hard Sell.</p>
  </section>

  <section class="faq">
    <div class="title">Frequently Asked Questions</div>
    <p class="sub">Lorem Ipsum Dolor Sit Amet Consectetur. Lobortis Neque Arcu.</p>
    <div class="faq-open"><h5>What age groups do you train?<span>–</span></h5><p>We offer classes for girls ages 3 to 17, from beginners taking their first steps in rhythmic gymnastics to competitive athletes training for national and international levels.</p></div>
    <div class="faq-item">How do I sign up for the Free Trial?<span>+</span></div>
    <div class="faq-item">Do you offer competitive training programs?<span>+</span></div>
    <div class="faq-item">Are parents allowed to watch the classes?<span>+</span></div>
    <div class="faq-item">How do I know which class is right for my child?<span>+</span></div>
    <span class="btn btn-outline">Have A Question Connect With Us</span>
  </section>

  <section class="connect-full">
    <svg class="wave" style="top:0;height:40px" viewBox="0 0 263 40" preserveAspectRatio="none"><path d="M0 30 Q130 -12 263 32" stroke="#4e92d6" stroke-width="2.5" fill="none"/></svg>
    <div class="title">Let's Connect</div>
    <p class="sub">Lorem Ipsum Dolor Sit Amet Consectetur. Lobortis Neque Arcu.</p>
    <div class="contact-head">Contact Information</div>
    <div class="contact-line"></div>
    <div class="contact-row"><svg viewBox="0 0 14 14"><path d="M7 13s-4-4.5-4-7.5a4 4 0 0 1 8 0C11 8.5 7 13 7 13z" stroke="#c060e0" fill="none"/><circle cx="7" cy="5.5" r="1.5" stroke="#c060e0" fill="none"/></svg>Maple Ridge, Corvale,<br>Westbrook,</div>
    <div class="contact-row"><svg viewBox="0 0 14 14"><path d="M3 1l3 3-2 2q2 3 4 4l2-2 3 3-2 2Q5 12 1 3z" stroke="#c060e0" fill="none"/></svg>+1 310-555-0142</div>
    <div class="contact-row"><svg viewBox="0 0 14 14"><rect x="1" y="3" width="12" height="8" stroke="#c060e0" fill="none"/><path d="M1 3l6 5 6-5" stroke="#c060e0" fill="none"/></svg>hello@taviskgym.com</div>
    <div class="follow">Follow Us on</div>
    <div class="socials"><i></i><i></i><i></i><i></i><i></i></div>
    <div class="contact-head" style="margin-top:40px">Timings</div>
    <div class="contact-line"></div>
    <div class="hours">
      <div><span>Monday</span><span>09:00 am – 05:00 pm</span></div>
      <div><span>Tuesday</span><span>09:00 am – 05:00 pm</span></div>
      <div><span>Wednesday</span><span>09:00 am – 05:00 pm</span></div>
      <div><span>Thursday</span><span>09:00 am – 05:00 pm</span></div>
      <div><span>Friday</span><span>09:00 am – 05:00 pm</span></div>
      <div><span>Saturday</span><span>Closed</span></div>
      <div><span>Sunday</span><span>Closed</span></div>
    </div>
    <div class="contact-head" style="margin-top:40px">Location</div>
    <div class="contact-line"></div>
    <div class="map" role="img" aria-label="Street map showing the gym location"></div>
  </section>

  <section class="footer">
    <svg class="wave" style="top:0;height:70px" viewBox="0 0 263 70" preserveAspectRatio="none"><path d="M0 0 L263 0 L263 8 Q220 60 120 44 Q50 34 0 40 Z" fill="#0c1440"/><path d="M263 8 Q220 60 120 44" stroke="#4e92d6" stroke-width="3" fill="none"/></svg>
    <div class="footer-brand"><b></b>Tavisk Gymnastics</div>
    <p>Lorem Ipsum Dolor Sit Amet, Consectetur Adipiscing Elit, Sed Do Eiusmod Tempor Incididunt Ut Labore Et Dolore Magna Aliqua.</p>
    <a>Read More</a>
    <div class="f-label">Follow Us on</div>
    <div class="socials"><i></i><i></i><i></i></div>
    <div class="f-head">Quick Links</div>
    <ul class="f-links"><li>Home</li><li>About</li><li>Classes &amp; Programs</li><li>News &amp; Events</li><li>Contact Us</li></ul>
    <div class="f-head">Contact Information</div>
    <div class="f-contact"><svg viewBox="0 0 14 14"><path d="M7 13s-4-4.5-4-7.5a4 4 0 0 1 8 0C11 8.5 7 13 7 13z" stroke="#c060e0" fill="none"/></svg>Serving Your Business Needs In LA &amp; OC.</div>
    <div class="f-contact"><svg viewBox="0 0 14 14"><path d="M3 1l3 3-2 2q2 3 4 4l2-2 3 3-2 2Q5 12 1 3z" stroke="#c060e0" fill="none"/></svg>+1 310-555-0142</div>
    <div class="f-contact"><svg viewBox="0 0 14 14"><rect x="1" y="3" width="12" height="8" stroke="#c060e0" fill="none"/><path d="M1 3l6 5 6-5" stroke="#c060e0" fill="none"/></svg>team@taviskgym.com</div>
    <div class="f-head">Newsletter</div>
    <div class="f-label" style="margin-top:6px">Subscribe to our Newsletter!</div>
    <div class="news">Email Address<i><svg width="12" height="8" viewBox="0 0 12 8"><path d="M0 4h10 M7 1l3 3-3 3" stroke="#fff" fill="none"/></svg></i></div>
    <div class="copy">© Tavisk Gymnastics– All rights reserved<br><span>Terms and Conditions &nbsp; | &nbsp; Privacy Policy</span></div>
  </section>
</div>

</body>
</html>
```